Waste Oil Filter collection & disposal

Basically I need a 1 page website for the business called Brenmoor Waste Solutions.
We are a environmental service provider and we collect and dispose of waste oil filters to protect the environment from hazardous waste oil products.

This is the link to our current website: www.brenmoorwaste.co.nz

we want it to look fresh and better than our current website. we may potentially look at getting a new logo designed and are open to ideas/designs if you have any.

Industry/Entity Type

Business

Logo Text

Brenmoor Waste Solutions

Number of Pages Required

1 page

Requirements
Must have
• same colours as current website.
• description of what service we provide please refer to leaflet attached

```html
<!DOCTYPE html>
<html lang="en">
<head>
<meta charset="utf-8">
<title>Brenmoor Waste Solutions Ltd – Oil Filter Collection &amp; Disposal</title>
<link rel="stylesheet" href="https://fonts.googleapis.com/css2?family=Montserrat:wght@400;500;600;700&display=swap">
<style>
:root{
  --navy:#134a7c;
  --green:#5a8f5f;
  --green-text:#4f8a55;
  --sand:#efeeec;
  --ink:#2b2b2b;
  --muted:#555;
  --white:#fff;
  --icon:#8a9aab;
}
*{box-sizing:border-box;margin:0;padding:0}
html,body{width:1200px;height:2161px;overflow:hidden}
body{position:relative;font-family:'Montserrat',sans-serif;color:var(--ink);background:var(--white)}
.abs{position:absolute}

/* header */
.site-header{position:absolute;left:0;top:0;width:1200px;height:118px;background:var(--white)}
.brand-mark{position:absolute;left:250px;top:38px;width:64px;height:64px;border-radius:50%;background:var(--green)}
.brand-name{position:absolute;left:335px;top:38px;font-size:22px;font-weight:700;color:#333}
.brand-tag{position:absolute;left:335px;top:72px;font-size:15px;font-weight:500;color:#444}

/* nav */
.main-nav{position:absolute;left:0;top:118px;width:1200px;height:57px;background:var(--navy);color:var(--white)}
.main-nav a{position:absolute;top:18px;font-size:16px;font-weight:700;color:var(--white);text-decoration:none}
.connect{position:absolute;left:795px;top:18px;font-size:16px;font-weight:700}
.social{position:absolute;top:14px;width:28px;height:28px;border-radius:50%}
.social.dark{background:var(--white)}
.social.light{background:var(--icon)}

/* hero */
.hero{position:absolute;left:0;top:175px;width:1200px;height:336px;
  background:radial-gradient(circle at 30% 40%,#5a4a3a 0,#3a3c3f 30%,#2a2e33 60%),linear-gradient(90deg,#3c3530,#2d3640,#3a3a34)}
.hero-text{position:absolute;left:250px;top:78px;width:700px;text-align:center;color:var(--white);font-size:23px;font-weight:700;line-height:35.5px}
.btn-learn{position:absolute;left:541px;top:194px;width:105px;height:28px;background:var(--green);color:var(--white);font-size:12px;font-weight:700;text-align:center;line-height:28px;border-radius:2px}

/* services */
.services{position:absolute;left:0;top:511px;width:1200px;height:483px;background:var(--sand)}
.section-title{font-size:24px;font-weight:700;color:var(--navy)}
.services .section-title{position:absolute;left:150px;top:28px}
.services-intro{position:absolute;left:150px;top:70px;width:600px;font-size:16px;line-height:22px;color:#333}
.photo{background:linear-gradient(160deg,#8a9a8e,#4f6a5e)}
.svc-photo{position:absolute;top:160px;width:179px;height:135px;border-radius:3px}
.svc-title{position:absolute;top:313px;font-size:15px;font-weight:700;color:var(--green-text)}
.svc-text{position:absolute;top:337px;font-size:12px;line-height:22px;color:#333}
.svc-text .col{display:inline-block;width:120px}
.bin{position:absolute;left:849px;top:230px;width:163px;height:222px;border-radius:10px 10px 16px 16px;background:linear-gradient(180deg,#3a3a3a,#1e1e1e)}

/* gallery */
.gallery .section-title{position:absolute;left:155px;top:1019px}
.card{position:absolute;width:281px;height:322px;background:var(--sand);box-shadow:0 1px 4px rgba(0,0,0,.35);border-radius:2px;overflow:hidden}
.card-photo{height:241px}
.card-title{position:absolute;left:8px;top:252px;font-size:15px;font-weight:700;color:#333}
.card-desc{position:absolute;left:8px;top:273px;font-size:12px;color:#333}
.card-more{position:absolute;left:6px;top:296px;font-size:11px;font-weight:700;color:var(--navy)}
.card-share{position:absolute;left:145px;top:296px;font-size:11px;font-weight:700;color:var(--navy)}
.card .dot{position:absolute;top:291px;width:22px;height:22px;border-radius:50%}
.dot.d1{left:190px;background:var(--navy)}
.dot.d2,.dot.d3{background:var(--icon)}
.dot.d2{left:220px}.dot.d3{left:249px}

/* contact */
.contact{position:absolute;left:0;top:1767px;width:1200px;height:349px;background:var(--sand)}
.contact h3{position:absolute;font-size:15px;font-weight:700;color:#333}
.field{position:absolute;background:var(--white);border-radius:5px;font-size:12px;color:#444;padding:12px 17px}
.btn-send{position:absolute;left:170px;top:254px;width:100px;height:40px;background:var(--navy);color:var(--white);border-radius:4px;font-size:13px;font-weight:700;text-align:center;line-height:40px}
.info{position:absolute;font-size:12px;color:#555;line-height:18px}
.map{position:absolute;left:843px;top:146px;width:136px;height:92px;background:linear-gradient(135deg,#dfe6d8,#c9d6c4)}
.map-bar{position:absolute;left:843px;top:223px;width:136px;height:15px;background:var(--green)}

/* footer */
.site-footer{position:absolute;left:0;top:2116px;width:1200px;height:45px;background:var(--green);font-size:11px;color:#2f4a32}
.site-footer span{position:absolute;top:16px}
</style>
</head>
<body>

<header class="site-header">
  <div class="brand-mark"></div>
  <div class="brand-name">Brenmoor Waste Solutions Ltd</div>
  <div class="brand-tag">Oil Filter Collection &amp; Disposal Service</div>
</header>

<nav class="main-nav">
  <a href="#" style="left:151px">Home</a>
  <a href="#" style="left:273px">Gallery</a>
  <a href="#" style="left:397px">Services</a>
  <a href="#" style="left:536px">About Us</a>
  <span class="connect">Connect with us:</span>
  <span class="social dark" style="left:941px"></span>
  <span class="social light" style="left:979px"></span>
  <span class="social light" style="left:1016px"></span>
</nav>

<section class="hero" role="img" aria-label="Blurred pile of used oil filters">
  <p class="hero-text">Brenmoor Waste Solutions Ltd specialize in the collection &amp; disposal of oil / fuel filters, servicing the lower north island on a monthly cycle.</p>
  <div class="btn-learn">Learn More</div>
</section>

<section class="services">
  <h2 class="section-title">Services We Offer</h2>
  <p class="services-intro">We offer a cost effective environmentally friendly system for the collection and disposal of waste oil filters helping minimise contamination of landfills keeping your industry compliant.</p>

  <div class="svc-photo photo" style="left:151px" role="img" aria-label="Green and white collection truck"></div>
  <h3 class="svc-title" style="left:151px">The Process</h3>
  <p class="svc-text" style="left:151px">Filters are collected and transported back<br>to the processing plant.<br>At the processing plant they are:<br>
    <span class="col">• Drained</span>• Crushed into bricks<br>
    <span class="col">• Sorted</span>• Drained a third time<br>
    <span class="col">• Drained again</span>• Stacked ready for Metal Recycling</p>

  <div class="svc-photo photo" style="left:548px;background:linear-gradient(160deg,#6a6f78,#2e3340)" role="img" aria-label="Crushed oil filters"></div>
  <h3 class="svc-title" style="left:548px">What Happens to the Oil</h3>
  <p class="svc-text" style="left:548px">All residual oil is collected into our<br>tank and then recycled.<br>Currently we are processing over 2,000<br>litres of oil amonth.</p>

  <div class="bin" role="img" aria-label="Dark grey wheelie bin for filter collection"></div>
</section>

<section class="gallery">
  <h2 class="section-title">Gallery</h2>

  <article class="card" style="left:153px;top:1071px">
    <div class="card-photo photo" role="img" aria-label="Collection truck"></div>
    <div class="card-title">Vehicles</div><div class="card-desc">Purpose built truck for collection</div>
    <span class="card-more">Read More</span><span class="card-share">Share:</span>
    <span class="dot d1"></span><span class="dot d2"></span><span class="dot d3"></span>
  </article>
  <article class="card" style="left:458px;top:1071px">
    <div class="card-photo photo" style="background:linear-gradient(160deg,#b8bcb8,#2f7a5e)" role="img" aria-label="Green filter press machine"></div>
    <div class="card-title">Filter Press</div><div class="card-desc">Baler</div>
    <span class="card-more">Read More</span><span class="card-share">Share:</span>
    <span class="dot d1"></span><span class="dot d2"></span><span class="dot d3"></span>
  </article>
  <article class="card" style="left:761px;top:1071px">
    <div class="card-photo photo" style="background:linear-gradient(160deg,#7d8a86,#2f6e62)" role="img" aria-label="Filter processing machine"></div>
    <div class="card-title">Filter processing machine</div><div class="card-desc">This machine extracts 96% of the oil left.....</div>
    <span class="card-more">Read More</span><span class="card-share">Share:</span>
    <span class="dot d1"></span><span class="dot d2"></span><span class="dot d3"></span>
  </article>

  <article class="card" style="left:153px;top:1419px">
    <div class="card-photo photo" style="background:linear-gradient(160deg,#a9b0a6,#2f7a62)" role="img" aria-label="Filter bailer in workshop"></div>
    <div class="card-title">Filter Bailer</div>
    <span class="card-more">Read More</span><span class="card-share">Share:</span>
    <span class="dot d1"></span><span class="dot d2"></span><span class="dot d3"></span>
  </article>
  <article class="card" style="left:458px;top:1419px">
    <div class="card-photo photo" style="background:linear-gradient(160deg,#6e737c,#23705e)" role="img" aria-label="Brick of crushed filters"></div>
    <div class="card-title">Brick of filters</div><div class="card-desc">A brick of filters 96% oil free</div>
    <span class="card-more">Read More</span><span class="card-share">Share:</span>
    <span class="dot d1"></span><span class="dot d2"></span><span class="dot d3"></span>
  </article>
  <article class="card" style="left:761px;top:1419px">
    <div class="card-photo photo" style="background:linear-gradient(160deg,#7a7f88,#b08a5e)" role="img" aria-label="Pallet of filter bricks"></div>
    <div class="card-title">Pallet of bricks</div><div class="card-desc">Pallet of bricks ready for transport to .....</div>
    <span class="card-more">Read More</span><span class="card-share">Share:</span>
    <span class="dot d1"></span><span class="dot d2"></span><span class="dot d3"></span>
  </article>
</section>

<section class="contact">
  <h3 style="left:170px;top:50px">Send us a message</h3>
  <div class="field" style="left:170px;top:97px;width:206px;height:35px">Full name</div>
  <div class="field" style="left:391px;top:97px;width:206px;height:35px">Email address</div>
  <div class="field" style="left:170px;top:149px;width:427px;height:89px">Message</div>
  <div class="btn-send">SEND</div>

  <h3 style="left:843px;top:50px">Contact Us</h3>
  <p class="info" style="left:843px;top:73px">PHONE &nbsp;06 555 0148</p>
  <h3 style="left:843px;top:118px">Reach Us</h3>
  <div class="map" role="img" aria-label="Location map"></div>
  <div class="map-bar"></div>
  <p class="info" style="left:847px;top:250px">OPENING HOURS<br>Monday - Friday<br>7.30am - 5.00pm</p>
</section>

<footer class="site-footer">
  <span style="left:161px">Copyright @ Brenmoor Waste Solutions Ltd</span>
  <span style="left:690px">Privacy policy</span>
  <span style="left:780px">|</span>
  <span style="left:801px">Terms and conditions</span>
  <span style="left:934px">|</span>
  <span style="left:957px">Company information</span>
</footer>

</body>
</html>
```